Business Card for my New Brokerage

Looking to get a business card design for my new Real Estate Brokerage.
I want it with Picture, Phone Number, Email, Website, Office Address
Name and Designation. Please add logo too.

Target Market(s)

Real Estate Investors or Home Buyers

Industry/Entity Type

Real Estate

Contact Information for Business Card

Name, Email, Phone Number, website, email, office address

Colors
EB3D1F
EC4F4E
F09395
F8D3D4
FCEDEE

Requirements
Must have
• Minimalistic, Clean, Modern, Photo
Nice to have
• White and Red Colors

```html
<!DOCTYPE html>
<html lang="en">
<head>
<meta charset="utf-8">
<title>Halden Realty Inc – Business Card</title>
<link href="https://fonts.googleapis.com/css2?family=Poppins:wght@400;500;600;700&display=swap" rel="stylesheet">
<style>
  :root{
    --brand-red:#dd1f26;
    --brand-orange:#eb5a2a;
    --brand-amber:#f6c98a;
    --brand-gold:#e6c46a;
    --ink:#111111;
    --paper:#ffffff;
    --stage:#ece9e4;
    --photo-tone-a:#cfcdd1;
    --photo-tone-b:#a3a4aa;
  }
  *{margin:0;padding:0;box-sizing:border-box}
  html,body{width:900px;height:1200px;overflow:hidden}
  body{background:var(--stage);font-family:"Poppins",sans-serif;position:relative}

  .card{position:absolute;left:82px;width:733px;height:428px;border-radius:22px;overflow:hidden;box-shadow:0 6px 14px rgba(0,0,0,.18)}
  .card--front{top:137px;background:var(--paper)}
  .card--back{top:633px;background:var(--brand-red)}

  .front-art{position:absolute;left:0;top:0;width:733px;height:428px}
  .agent-photo{position:absolute;left:26px;top:30px;width:286px;height:398px;border-radius:6px 6px 0 0;background:linear-gradient(180deg,var(--photo-tone-a),var(--photo-tone-b))}

  .wordmark{position:absolute;font-weight:600;line-height:1.12;letter-spacing:1px}
  .card--front .wordmark{right:40px;top:62px;width:300px;text-align:right;color:var(--brand-red);font-size:40px}
  .card--back .wordmark{left:0;right:0;top:150px;text-align:center;color:var(--paper);font-size:56px}

  .agent{position:absolute;right:38px;top:196px;text-align:right}
  .agent__name{font-size:25px;font-weight:700;color:var(--ink);letter-spacing:.5px;line-height:1.1}
  .agent__role{font-size:16px;color:var(--brand-red);letter-spacing:.5px;margin-top:2px}

  .contact{position:absolute;right:38px;top:263px;list-style:none;font-size:16px;color:var(--ink)}
  .contact li{display:flex;justify-content:flex-end;align-items:center;height:25px;text-align:right}
  .contact li.contact__address{height:50px;margin-top:9px;align-items:flex-start;text-align:left}
  .contact svg{width:15px;height:15px;margin-left:12px;flex:none;fill:var(--brand-red)}
  .contact__address svg{margin-top:5px}
  .contact__address span{line-height:25px}

  .back-url{position:absolute;left:0;right:0;top:366px;text-align:center;color:var(--paper);font-size:16px;font-weight:500;letter-spacing:2px}
</style>
</head>
<body>

<section class="card card--front">
  <svg class="front-art" viewBox="0 0 733 428" aria-hidden="true">
    <defs>
      <linearGradient id="chevronFill" x1="0" y1="1" x2="1" y2="0">
        <stop offset="0" stop-color="var(--brand-amber)"/>
        <stop offset=".35" stop-color="var(--brand-orange)"/>
        <stop offset="1" stop-color="var(--brand-red)"/>
      </linearGradient>
    </defs>
    <polygon points="0,0 258,0 383,213 250,428 0,428" fill="url(#chevronFill)"/>
    <polyline points="276,0 404,213 272,428" fill="none" stroke="var(--brand-gold)" stroke-width="9"/>
  </svg>
  <div class="agent-photo" role="img" aria-label="Portrait photo of the realtor in a grey suit, arms crossed"></div>

  <p class="wordmark">HALDEN REALTY INC</p>

  <div class="agent">
    <p class="agent__name">DANIEL MORENO</p>
    <p class="agent__role">REALTOR</p>
  </div>

  <ul class="contact">
    <li><span>214-555-0142</span>
      <svg viewBox="0 0 24 24"><path d="M6.6 10.8a15.1 15.1 0 0 0 6.6 6.6l2.2-2.2c.3-.3.7-.4 1-.2 1.1.4 2.3.6 3.6.6.6 0 1 .4 1 1V20c0 .6-.4 1-1 1A17 17 0 0 1 3 4c0-.6.4-1 1-1h3.5c.6 0 1 .4 1 1 0 1.3.2 2.5.6 3.6.1.3 0 .7-.2 1z"/></svg></li>
    <li><span>info@haldenrealty.com</span>
      <svg viewBox="0 0 24 24"><path d="M2 5h20v14H2z"/><path d="M2 5l10 8 10-8z" fill="#fff" opacity=".55"/></svg></li>
    <li><span>www.haldenrealty.com</span>
      <svg viewBox="0 0 24 24"><path d="M12 2a10 10 0 1 0 0 20 10 10 0 0 0 0-20zm0 2c.9 1.2 1.6 2.6 2 4h-4c.4-1.4 1.1-2.8 2-4zM9.6 10h4.8a12 12 0 0 1 0 4H9.6a12 12 0 0 1 0-4zM4.3 10h3.3a14 14 0 0 0 0 4H4.3a8 8 0 0 1 0-4zm12.1 0h3.3a8 8 0 0 1 0 4h-3.3a14 14 0 0 0 0-4zM5.3 8a8 8 0 0 1 3.6-3.4A14 14 0 0 0 7.9 8zm10.8 0a14 14 0 0 0-1-3.4A8 8 0 0 1 18.7 8zM5.3 16h2.6a14 14 0 0 0 1 3.4A8 8 0 0 1 5.3 16zm4.7 0h4c-.4 1.4-1.1 2.8-2 4-.9-1.2-1.6-2.6-2-4zm6.1 0h2.6a8 8 0 0 1-3.6 3.4 14 14 0 0 0 1-3.4z"/></svg></li>
    <li class="contact__address"><span>118 Harbor Street West<br>Suite 210, Lakeview</span>
      <svg viewBox="0 0 24 24"><path d="M12 2a7 7 0 0 0-7 7c0 5.3 7 13 7 13s7-7.7 7-13a7 7 0 0 0-7-7zm0 9.5A2.5 2.5 0 1 1 12 6.5a2.5 2.5 0 0 1 0 5z"/></svg></li>
  </ul>
</section>

<section class="card card--back">
  <p class="wordmark">HALDEN<br>REALTY INC</p>
  <p class="back-url">WWW.HALDENREALTY.COM</p>
</section>

</body>
</html>
```